Business cards Dör Kornhüüs GmbH & Co.KG

We need a uniform business card design template for our employees.
A template should be created to have the same design for all business cards.

Contact Information for Business Card

Firma und Firmierung, Name, Funktion in Unternehmen, Anschrift, Tel. Handynummer, Emailadresse, Internetseite

Colors

Designer to choose colors to be used in the design.

Requirements
Must have
• Our company logo must be on it

```html
<!DOCTYPE html>
<html lang="de">
<head>
<meta charset="utf-8">
<title>Dör Kornhüüs GmbH &amp; Co.KG – Visitenkarte</title>
<link href="https://fonts.googleapis.com/css2?family=Arimo:wght@400&family=EB+Garamond:wght@600&display=swap" rel="stylesheet">
<style>
  :root {
    --page-bg: #ece9e6;
    --card-bg: #ffffff;
    --rose: #f27383;
    --lilac: #c99fcb;
    --text-grey: #4a4a4a;
    --card-shadow: 0 4px 10px rgba(0,0,0,0.35);
  }
  * { margin: 0; padding: 0; box-sizing: border-box; }
  html, body {
    width: 1125px; height: 1200px; overflow: hidden;
    background: var(--page-bg);
    font-family: "Arimo", Arial, sans-serif;
  }
  .canvas { position: relative; width: 1125px; height: 1200px; }

  .card {
    position: absolute; left: 150px; width: 826px; height: 470px;
    background: var(--card-bg);
    border-radius: 22px;
    overflow: hidden;
    box-shadow: var(--card-shadow);
  }
  .card--front { top: 99px; }
  .card--back { top: 632px; }
  .card__band { position: absolute; left: 0; right: 0; height: 18px; }
  .card__band--top { top: 0; background: var(--rose); }
  .card__band--bottom { bottom: 0; background: var(--lilac); }

  .identity {
    position: absolute; right: 407px; top: 170px;
    text-align: right; color: var(--text-grey);
  }
  .identity__name {
    font-family: "EB Garamond", Georgia, serif; font-weight: 600;
    font-size: 29px; color: var(--lilac); letter-spacing: 0.3px; line-height: 30px;
  }
  .identity__role { font-size: 17px; color: var(--rose); line-height: 22px; margin-bottom: 4px; }
  .identity__line { font-size: 17.5px; line-height: 24px; }

  .divider {
    position: absolute; left: 443px; top: 174px; width: 1px; height: 118px;
    background: var(--lilac);
  }

  .contacts { position: absolute; left: 466px; top: 175px; list-style: none; }
  .contacts__item {
    display: flex; align-items: center; gap: 9px;
    font-size: 17.5px; line-height: 23.5px; color: var(--text-grey);
  }
  .contacts__icon { width: 18px; height: 18px; flex: none; }

  .brand {
    position: absolute; left: 0; right: 0; top: 205px;
    display: flex; justify-content: center; align-items: center; gap: 18px;
  }
  .brand__dot { width: 22px; height: 22px; border-radius: 50%; background: var(--lilac); }
  .brand__name {
    font-family: "Arimo", Arial, sans-serif; font-weight: 400;
    font-size: 58px; color: var(--lilac); letter-spacing: 1px;
  }
</style>
</head>
<body>
<main class="canvas">

  <section class="card card--front" aria-label="Vorderseite der Visitenkarte">
    <div class="card__band card__band--top"></div>

    <div class="identity">
      <p class="identity__name">JONAS ELLERBY</p>
      <p class="identity__role">President</p>
      <p class="identity__line">Dör Kornhüüs Nordische Backkunst</p>
      <p class="identity__line">42 Harbor Mill Road</p>
      <p class="identity__line">Kenai, Alaska 99611</p>
    </div>

    <div class="divider"></div>

    <ul class="contacts">
      <li class="contacts__item">
        <svg class="contacts__icon" viewBox="0 0 18 18" aria-hidden="true"><circle cx="9" cy="9" r="9" fill="#c99fcb"/><path d="M6 4.5l1.8 2-1 1.2c.6 1.4 1.6 2.4 3 3l1.2-1 2 1.8-1.2 1.6C8.8 13 5 9.2 4.9 6z" fill="#fff"/></svg>
        555-208-4417
      </li>
      <li class="contacts__item">
        <svg class="contacts__icon" viewBox="0 0 18 18" aria-hidden="true"><circle cx="9" cy="9" r="9" fill="#c99fcb"/><rect x="6" y="3.8" width="6" height="10.4" rx="1.2" fill="#fff"/><rect x="7" y="5" width="4" height="7" fill="#c99fcb"/></svg>
        555-630-1952
      </li>
      <li class="contacts__item">
        <svg class="contacts__icon" viewBox="0 0 18 18" aria-hidden="true"><circle cx="9" cy="9" r="9" fill="#c99fcb"/><rect x="6" y="4" width="6" height="3" fill="#fff"/><rect x="4" y="7.5" width="10" height="5" rx="1" fill="#fff"/><rect x="6" y="10.5" width="6" height="3" fill="#fff" stroke="#c99fcb" stroke-width=".6"/></svg>
        555-744-2089
      </li>
      <li class="contacts__item">
        <svg class="contacts__icon" viewBox="0 0 18 18" aria-hidden="true"><circle cx="9" cy="9" r="9" fill="#c99fcb"/><rect x="4.2" y="5.5" width="9.6" height="7" rx=".8" fill="#fff"/><path d="M4.5 6l4.5 3.6L13.5 6" fill="none" stroke="#c99fcb" stroke-width="1"/></svg>
        info@doerkornhuus.com
      </li>
      <li class="contacts__item">
        <svg class="contacts__icon" viewBox="0 0 18 18" aria-hidden="true"><circle cx="9" cy="9" r="9" fill="#c99fcb"/><circle cx="9" cy="9" r="4.8" fill="none" stroke="#fff" stroke-width="1.3"/><path d="M4.2 9h9.6M9 4.2c-2 2.8-2 6.8 0 9.6M9 4.2c2 2.8 2 6.8 0 9.6" fill="none" stroke="#fff" stroke-width=".9"/></svg>
        www.doerkornhuus.com
      </li>
    </ul>

    <div class="card__band card__band--bottom"></div>
  </section>

  <section class="card card--back" aria-label="Rückseite der Visitenkarte">
    <div class="card__band card__band--top"></div>
    <div class="brand">
      <span class="brand__dot"></span>
      <span class="brand__name">Dör Kornhüüs</span>
    </div>
    <div class="card__band card__band--bottom"></div>
  </section>

</main>
</body>
</html>
```